Business Intelligence Application - Reporting Menu and Report Criteria Design

Looking for a fresh, effective and user friendly view for the menu structure and reporting criteria screen format for a business reporting application. Initial format completed, content structure is in place, but we need the 'wow' design.. as its a serious professional report/BI tool it has to fall within certain guidelines for clarity and graphics..but we want it to be slick, friendly, great user experience. There is a large amount of complex content to fit into a small space and we need it to be very inviting, modern and intuitive.. If interested, please review the attachment. We have live screens in operation, but feel these could be improved and looking forward to seeing what great creative suggestions could be made. Please review work done to date in the attached.. We are not looking for a total re-design of everything, all the basic business content/structure is there.. but tell us what we could do to improve this in terms of graphic design... particularly the criteria screens.. thanks!
Updates

Reason: Need a few more days to review designs - thanks for all submissions so far, we will make a selection shortly.

Target Market(s)

Business analysts, hotel operations teams, finance analysts hospitality industry

Industry/Entity Type

Hospitality

Coding

Coded - Design and coding required

Number of Pages Required

4 page

Font styles to use
Sans Serif
Other font styles liked:
• Candara, please see example in deck

Colors
3276b5
3176b5
0255a3
85acd3
33a6d7
cee9f5
85cae6

Requirements
Must have
• sharp clear, logical menu structure, (currently it has 'clicks to sub-menus, we need hover over, slide to sub-menus..) colour, styling.. and most focus on revision of criteria.. right now is somewhat heavy, cumbersome.. keep colour and friendly intuitive process steps.. its heavy analytical stuff.. best of luck!
Should not have
• No grey fonts on white or grey screens! many business apps are not readable or sharp.. or fonts are too small.. colourless, so please avoid that.. see our deck - sharp dark (navy) or black fonts on white, or light shading..

```html
<!DOCTYPE html>
<html lang="en">
<head>
<meta charset="utf-8">
<title>Silver Bay Hotel &amp; Suites — Rooms Performance</title>
<link href="https://fonts.googleapis.com/css2?family=Cabin:wght@400;500;600&family=Roboto+Condensed:wght@400;500&display=swap" rel="stylesheet">
<style>
:root{
  --page:#e4e4e4;
  --navy:#0c1a3c;
  --head-a:#17244f;
  --head-b:#4a5c98;
  --nav-dark:#0a1538;
  --nav-blue:#8fb3e6;
  --nav-grey:#d2d2d2;
  --tools:#555a60;
  --strip:#e9e9e9;
  --th:#9fbfe2;
  --th-line:#ffffff;
  --total:#78a6dd;
  --cell-a:#ffffff;
  --cell-b:#c9dcf1;
  --section-a:#4e4e50;
  --section-b:#c6c6c6;
  --section-rest:#d9d9d9;
  --ink:#0c1a3c;
  --white:#ffffff;
  --accent:#33a6d7;
}
*{box-sizing:border-box;margin:0;padding:0}
html,body{width:1200px;height:688px;overflow:hidden;background:var(--page);font-family:"Cabin",sans-serif;color:var(--ink)}
.app{position:absolute;left:11px;top:11px;width:1178px}
.topbar{height:53px;background:linear-gradient(90deg,var(--head-a),var(--head-b));display:flex;align-items:center;color:var(--white)}
.brand{display:flex;align-items:center;gap:12px;padding-left:20px;flex:1;font-size:16px;font-weight:500}
.brand-mark{width:26px;height:26px;border-radius:50%;background:var(--accent)}
.top-item{height:100%;display:flex;align-items:center;gap:10px;border-left:1px solid rgba(255,255,255,.35);padding:0 16px;font-size:11px;font-weight:500}
.top-item.user{width:140px}
.top-item.date{width:133px;line-height:1.2}
.top-item.icon{width:53px;justify-content:center;padding:0}
.mainnav{display:flex;gap:3px;margin-top:5px;height:30px}
.mainnav a{display:flex;align-items:center;justify-content:center;font-family:"Roboto Condensed",sans-serif;font-size:11px;font-weight:500;text-decoration:none;background:var(--nav-dark);color:var(--white)}
.mainnav a.soft{background:var(--nav-blue);color:var(--ink)}
.mainnav a.muted{background:var(--nav-grey);color:var(--ink)}
.mascot-slot{width:58px;background:var(--nav-grey);display:flex;align-items:center;justify-content:center}
.mascot-slot span{width:20px;height:20px;border-radius:50%;background:#c98a3e;display:block}
.toolbar{display:flex;height:30px;margin-top:4px;background:var(--strip);font-family:"Roboto Condensed",sans-serif;font-size:10.5px}
.tools{width:71px;background:var(--tools);color:var(--white);display:flex;align-items:center;gap:6px;padding-left:6px}
.criteria-label{display:flex;align-items:center;padding-left:25px;color:#222}
.workspace{background:var(--white);height:482px;padding-top:30px}
.report{width:100%;border-collapse:collapse;table-layout:fixed;font-size:11.5px}
.report col.label{width:191px}.report col.total{width:76px}
.report thead th{background:var(--th);font-weight:400;color:var(--ink);border-left:1px solid var(--th-line);height:23px}
.report thead th.range{text-align:left;padding-left:25px;font-size:11px;line-height:1.25;border-left:0;border-radius:6px 0 0 0}
.report thead tr:first-child th.day{border-bottom:1px solid var(--th-line)}
.report thead th.day:last-child{border-radius:0 6px 0 0}
.section td{height:15px;padding:0}
.section td.name{background:linear-gradient(90deg,var(--section-a),var(--section-b));color:var(--white);padding-left:25px;font-size:11.5px}
.section td.rest{background:var(--section-rest)}
.data td{height:23.2px;text-align:center;background:linear-gradient(180deg,var(--cell-a),var(--cell-b));font-size:10px}
.data td.name{text-align:left;padding-left:25px;font-size:11.5px;background:linear-gradient(90deg,var(--cell-b),var(--cell-a))}
.data td.total{background:var(--total)}
.footer{height:60px;margin-top:0;background:var(--navy);display:flex;align-items:center;justify-content:center;gap:10px;color:var(--white);font-size:15px;font-weight:500}
.footer-mark{width:24px;height:24px;border-radius:50%;background:var(--accent)}
</style>
</head>
<body>
<div class="app">
  <header class="topbar">
    <div class="brand"><span class="brand-mark"></span>Silver Bay Hotel &amp; Suites</div>
    <div class="top-item user">
      <svg width="22" height="22" viewBox="0 0 22 22" fill="#fff"><circle cx="11" cy="6" r="5"/><path d="M1 22c0-6 4-9 10-9s10 3 10 9z"/></svg>
      Welcome Admin
    </div>
    <div class="top-item date">
      <svg width="22" height="22" viewBox="0 0 22 22" fill="none" stroke="#fff" stroke-width="1.6"><rect x="2" y="4" width="18" height="16" rx="1"/><path d="M2 9h18M7 2v4M15 2v4"/><g fill="#fff" stroke="none"><rect x="5" y="11" width="2" height="2"/><rect x="9" y="11" width="2" height="2"/><rect x="13" y="11" width="2" height="2"/><rect x="5" y="15" width="2" height="2"/><rect x="9" y="15" width="2" height="2"/><rect x="13" y="15" width="2" height="2"/></g></svg>
      <div>Tuesday<br>October 3, 2017</div>
    </div>
    <div class="top-item icon">
      <svg width="20" height="22" viewBox="0 0 20 22" fill="#fff"><path d="M10 1c-4 0-6 3-6 7v5l-3 4h18l-3-4V8c0-4-2-7-6-7z"/><circle cx="10" cy="19.5" r="2.5"/></svg>
    </div>
    <div class="top-item icon">
      <svg width="22" height="22" viewBox="0 0 22 22" fill="none" stroke="#fff" stroke-width="2.4" stroke-linecap="round"><path d="M11 2v8"/><path d="M6 5a8 8 0 1 0 10 0"/></svg>
    </div>
  </header>

  <nav class="mainnav">
    <a style="width:72px">ADMIN</a>
    <a style="width:104px">MANAGEMENT</a>
    <a class="soft" style="width:143px">ROOMS PERFORMANCE</a>
    <a class="muted" style="width:130px">REVENUE SUMMARY</a>
    <a class="soft" style="width:112px">DEMAND &amp; RISK</a>
    <a class="muted" style="width:137px">INVENTORY ANALYSIS</a>
    <a class="muted" style="width:105px">PLACEHOLDER</a>
    <div class="mascot-slot" role="img" aria-label="Mascot shortcut icon"><span></span></div>
    <a style="width:125px">PROPERTY SEARCH</a>
    <a style="width:66px">INTEL</a>
    <a style="width:88px">PLANNING</a>
  </nav>

  <div class="toolbar">
    <div class="tools">
      <svg width="22" height="20" viewBox="0 0 22 20" stroke="#f0c040" stroke-width="2.4" stroke-linecap="round"><path d="M3 18L19 2M3 2l16 16"/></svg>
      TOOLS
    </div>
    <div class="criteria-label">SELECTED REPORT LABEL CRITERIA</div>
  </div>

  <main class="workspace">
    <table class="report">
      <colgroup><col class="label"><col class="total"><col span="12"></colgroup>
      <thead>
        <tr>
          <th class="range" rowspan="2">Aug 16, 2017 - Sept 30, 2017 -<br>Aug 17, 2016 - Oct 1, 2016</th>
          <th rowspan="2">Total</th>
          <th class="day">Aug 16</th><th class="day">Aug 17</th><th class="day">Aug 18</th><th class="day">Aug 19</th><th class="day">Aug 20</th><th class="day">Aug 21</th><th class="day">Aug 22</th><th class="day">Aug 23</th><th class="day">Aug 24</th><th class="day">Aug 25</th><th class="day">Aug 26</th><th class="day">Aug 27</th>
        </tr>
        <tr>
          <th>Wed</th><th>Thu</th><th>Fri</th><th>Sat</th><th>Sun</th><th>Mon</th><th>Tue</th><th>Wed</th><th>Thu</th><th>Fri</th><th>Sat</th><th>Sun</th>
        </tr>
      </thead>
      <tbody>
        <tr class="section"><td class="name">Occupancy</td><td class="rest" colspan="13"></td></tr>
        <tr class="data"><td class="name">Occupany Active Net</td><td class="total">0.0%</td><td>0.0%</td><td>0.0%</td><td>0.0%</td><td>0.0%</td><td>0.0%</td><td>0.0%</td><td>0.0%</td><td>0.0%</td><td>0.0%</td><td>0.0%</td><td>0.0%</td><td>0.0%</td></tr>
        <tr class="data"><td class="name">Occupany on the Books</td><td class="total">0.0%</td><td>0.0%</td><td>0.0%</td><td>0.0%</td><td>0.0%</td><td>0.0%</td><td>0.0%</td><td>0.0%</td><td>0.0%</td><td>0.0%</td><td>0.0%</td><td>0.0%</td><td>0.0%</td></tr>
        <tr class="data"><td class="name">Occupancy Gap</td><td class="total">0.0%</td><td>0.0%</td><td>0.0%</td><td>0.0%</td><td>0.0%</td><td>0.0%</td><td>0.0%</td><td>0.0%</td><td>0.0%</td><td>0.0%</td><td>0.0%</td><td>0.0%</td><td>0.0%</td></tr>
        <tr class="data"><td class="name">Net Available Rooms</td><td class="total">0</td><td>0</td><td>0</td><td>0</td><td>0</td><td>0</td><td>0</td><td>0</td><td>0</td><td>0</td><td>0</td><td>0</td><td>0</td></tr>
        <tr class="section"><td class="name">Rooms &amp; Demand Risk</td><td class="rest" colspan="13"></td></tr>
        <tr class="data"><td class="name">Active Rm Nights</td><td class="total">0</td><td>0</td><td>0</td><td>0</td><td>0</td><td>0</td><td>0</td><td>0</td><td>0</td><td>0</td><td>0</td><td>0</td><td>0</td></tr>
        <tr class="data"><td class="name">Risk Ratio Rm Nights</td><td class="total">0.0%</td><td>0.0%</td><td>0.0%</td><td>0.0%</td><td>0.0%</td><td>0.0%</td><td>0.0%</td><td>0.0%</td><td>0.0%</td><td>0.0%</td><td>0.0%</td><td>0.0%</td><td>0.0%</td></tr>
        <tr class="data"><td class="name">Active Avg Rm Rate</td><td class="total">0.0</td><td>0.0</td><td>0.0</td><td>0.0</td><td>0.0</td><td>0.0</td><td>0.0</td><td>0.0</td><td>0.0</td><td>0.0</td><td>0.0</td><td>0.0</td><td>0.0</td></tr>
        <tr class="data"><td class="name">Risk Ratio Avg Rm Rate</td><td class="total">0.0%</td><td>0.0%</td><td>0.0%</td><td>0.0%</td><td>0.0%</td><td>0.0%</td><td>0.0%</td><td>0.0%</td><td>0.0%</td><td>0.0%</td><td>0.0%</td><td>0.0%</td><td>0.0%</td></tr>
        <tr class="data"><td class="name">Active Rm Revenue</td><td class="total">0</td><td>0</td><td>0</td><td>0</td><td>0</td><td>0</td><td>0</td><td>0</td><td>0</td><td>0</td><td>0</td><td>0</td><td>0</td></tr>
        <tr class="data"><td class="name">Risk Ratio Rm Revenue</td><td class="total">0.0%</td><td>0.0%</td><td>0.0%</td><td>0.0%</td><td>0.0%</td><td>0.0%</td><td>0.0%</td><td>0.0%</td><td>0.0%</td><td>0.0%</td><td>0.0%</td><td>0.0%</td><td>0.0%</td></tr>
        <tr class="section"><td class="name">Occupancy</td><td class="rest" colspan="13"></td></tr>
        <tr class="data"><td class="name">Rm Nts OTB CY Def</td><td class="total">0</td><td>0</td><td>0</td><td>0</td><td>0</td><td>0</td><td>0</td><td>0</td><td>0</td><td>0</td><td>0</td><td>0</td><td>0</td></tr>
        <tr class="data"><td class="name">Rm Nts OTB Prior Def</td><td class="total">0</td><td>0</td><td>0</td><td>0</td><td>0</td><td>0</td><td>0</td><td>0</td><td>0</td><td>0</td><td>0</td><td>0</td><td>0</td></tr>
        <tr class="data"><td class="name">Difference</td><td class="total">0</td><td>0</td><td>0</td><td>0</td><td>0</td><td>0</td><td>0</td><td>0</td><td>0</td><td>0</td><td>0</td><td>0</td><td>0</td></tr>
        <tr class="data"><td class="name">% Variance</td><td class="total">0.0%</td><td>0.0%</td><td>0.0%</td><td>0.0%</td><td>0.0%</td><td>0.0%</td><td>0.0%</td><td>0.0%</td><td>0.0%</td><td>0.0%</td><td>0.0%</td><td>0.0%</td><td>0.0%</td></tr>
      </tbody>
    </table>
  </main>

  <footer class="footer"><span class="footer-mark"></span>Yield Atlas</footer>
</div>
</body>
</html>
```